大人ピアノ初心者が演奏する会場で、このコンサートのチラシを配る予定をしています。デザインは、タイトル名「星と祈りのロマンティック・ヴェルナスキ」を思わせるような雰囲気を希望しています。色は、「金色」を思わせるような飾りが一部ございますと、嬉しく存じます。写真は、添付資料をご参考下さいませ。
【社名】一般社団法人 日本ふわりキーボード会 【信念】「気軽・喜び・集い」の音楽を! 【公式ホームページ】http://www.fuwarikbd.jp 又は「ふわりキーボード」で検索。
A4
片面
「金色」を思わせるような、一部飾りを希望します。
デザインをご考案下さる方へ:

この度は、「星と祈りのロマンティック・ヴェルナスキ」コンサートのチラシをご検討・ご考案下さいまして、誠にありがとうございます。このプロジェクトは、選定確約しております。何卒お力添え下さいますよう、宜しくお願い申し上げます。

一般社団法人 日本ふわりキーボード会
添付資料につきまして「xls」書類のPDFを追加で添付致しますので、宜しくお願い申し上げます。
以下の点につきまして誠に恐縮ではございますが、訂正をお願い致します。

大阪青葉学院大学 ➝ 大阪翠嶺大学

以上でございます。何卒宜しくお願い申し上げます。
【デザインをご考案頂きました皆様へ】

この度は「星と祈りのロマンティック・ヴェルナスキ」のデザインをご考案頂きまして、
誠にありがとうございました。

素晴らしい作品ばかりで、本当に胸がいっぱいになるほど感謝でございます!

ご提案頂きました作品一点一点を、関係者と共に検討してまいりたいと存じます。

何卒宜しくお願い申し上げます。

取り急ぎ御礼まで。
デザインをご提案下さいました皆様へ:

この度は、「星と祈りのロマンティック・ヴェルナスキ」コンサートのチラシをご考案下さいまして、誠にありがとうございます。

あまりに素晴らしい作品の数々。。!!!
思わず見入るような工夫が随所になされており、感謝の念で一杯でございます。

デザイナー様の御言葉を拝読致しますと、作品をご考案されるにあたり資料を調べて下さったり、強い想いを込めてご考案されたり、ご覧になる方への年齢を考慮されたり。。とご配慮いただき、本当に頭が下がるような想いが致しました。

改めまして心より御礼申し上げます。

作品の選出おきましては、
企画メンバー全員が異なる作品を推薦するという事態となり、決定は困難を極めました。

しかし今回は、通常のコンサートではなく、
ヴェルナスキの人生について語ることがメインとなるコンサートですから、
下記の点を留意して検討致しました。

■ ヴェルナスキの手紙内容が読みやすい
■ 秘めた情熱が感じられる
■ ピアノの音色まで生き生きと感じる

今回は、ヴェルナスキのコンサートでしたが、
弊社は定期的に様々な企画をしてまいります。

どうぞ引き続き、今後共お力添え下さいますよう、
何卒宜しくお願い申し上げます。

心より感謝を込めて。。

一般社団法人 日本ふわりキーボード会
森下 千秋

この度は、「星と祈りのロマンティック・ヴェルナスキ」コンサートのチラシをご考案下さいまして、誠にありがとうございます。ご考案頂きました作品は、登場人物が浮かび上がるような訴え力があり、秘めた情熱が感じられました。ヴェルナスキの手紙内容も読みやすく、ピアノの音色も聴こえるかのようなデザインであると存じます。お陰様で、関係者共々大変喜んでおります。誠にありがとうございました。

この度は、「星と祈りのロマンティック・ヴェルナスキ」のチラシをご考案下さいまして、誠にありがとうございます。あまりにも素晴らしい作品の数々!思わず見入るような工夫が随所になされ、感謝の念で一杯でございます。作品の選出におきましては、企画メンバー全員が異なる作品を推薦するという事態となり、決定は困難を極めました。しかし、今回はヴェルナスキの人生や手紙内容・ヴェルナスキらしい情熱・ピアノの音色等が感じる作品をという観点で検討致しました。今後も企画をしてまいりたいと存じます。引き続き何卒宜しくお願い申し上げます。

```html
<!DOCTYPE html>
<html lang="ja">
<head>
<meta charset="utf-8">
<title>星と祈りのロマンティック・ヴェルナスキ</title>
<link href="https://fonts.googleapis.com/css2?family=Shippori+Mincho:wght@500;700;800&family=Noto+Sans+JP:wght@400;700&family=Cormorant+Garamond:ital,wght@1,600&display=swap" rel="stylesheet">
<style>
:root{
  --wine-dark:#3a0a12;
  --wine:#7a1424;
  --wine-light:#a52a3a;
  --gold:#d9b45a;
  --gold-light:#f4e2a4;
  --gold-deep:#a87d2c;
  --cream:#fbf5e6;
  --ink:#3b2a20;
  --line:#b99a5c;
}
*{margin:0;padding:0;box-sizing:border-box}
html,body{width:846px;height:1200px;overflow:hidden;background:#fff}
.flyer{position:relative;width:846px;height:1200px;font-family:"Shippori Mincho",serif;color:#fff;overflow:hidden}
.stage{position:absolute;inset:0 0 190px 0;background:radial-gradient(ellipse at 70% 30%,var(--wine-light) 0%,var(--wine) 40%,var(--wine-dark) 100%)}
.frame{position:absolute;inset:12px 12px 198px 12px;border:1.5px solid var(--gold);pointer-events:none}
.frame::after{content:"";position:absolute;inset:5px;border:0.8px solid var(--gold-deep)}
.portrait{position:absolute;right:24px;top:60px;width:330px;height:420px;background:radial-gradient(ellipse at 55% 40%,#e6cbb0 0%,#8a5a4a 35%,#3c1018 75%,transparent 100%);opacity:.9}
.piano{position:absolute;left:24px;top:560px;width:360px;height:110px;background:linear-gradient(160deg,#1a0508 0%,#4a1620 60%,transparent 100%);opacity:.85}
.kicker{position:absolute;top:30px;left:0;width:846px;text-align:center;font-size:24px;font-weight:700;color:var(--gold-light);letter-spacing:.12em}
.lead{position:absolute;top:66px;left:60px;width:726px;text-align:center;font-size:13px;line-height:1.6;color:var(--gold-light)}
.title{position:absolute;top:112px;left:40px;font-weight:800;line-height:1.15;text-shadow:0 2px 6px rgba(0,0,0,.5)}
.title .l1{display:block;font-size:52px;background:linear-gradient(180deg,var(--gold-light),var(--gold) 60%,var(--gold-deep));-webkit-background-clip:text;background-clip:text;color:transparent}
.title .l2{display:block;font-size:44px;color:#fff}
.title .en{position:absolute;top:18px;left:230px;font-family:"Cormorant Garamond",serif;font-style:italic;font-size:38px;color:rgba(244,226,164,.25);white-space:nowrap}
.timeline{position:absolute;top:262px;left:40px;width:520px;list-style:none}
.timeline li{font-size:15px;line-height:1.55;border-bottom:1px dotted rgba(217,180,90,.6);padding:3px 0;text-shadow:0 1px 3px #000;white-space:nowrap}
.timeline .age{color:var(--gold-light);font-weight:700;font-size:18px;margin-right:8px}
.timeline li:nth-child(2){padding-left:40px}.timeline li:nth-child(3){padding-left:70px}.timeline li:nth-child(4){padding-left:100px}.timeline li:nth-child(5){padding-left:130px}.timeline li:nth-child(6){padding-left:160px}.timeline li:nth-child(7){padding-left:190px}
.finale{position:absolute;top:538px;right:60px;font-size:24px;font-weight:700;color:var(--gold-light)}
.info{position:absolute;top:690px;left:40px;width:766px;font-family:"Noto Sans JP",sans-serif;color:#fff}
.row{display:flex;align-items:center;margin-bottom:8px;white-space:nowrap}
.label{flex:0 0 62px;font-size:13px;font-weight:700;color:var(--wine-dark);background:var(--gold);text-align:center;padding:2px 0;margin-right:12px;border-radius:2px;white-space:nowrap}
.date{font-family:"Shippori Mincho",serif;font-size:32px;font-weight:800;color:var(--gold-light);line-height:1.2}
.date small{font-size:18px}
.time{font-size:18px;margin-left:14px}
.val{font-size:15px;line-height:1.5}
.val strong{font-size:20px}
.fee{font-family:"Shippori Mincho",serif;font-size:28px;font-weight:800;color:var(--gold-light);line-height:1.2;margin-right:4px}
.org{display:flex;align-items:center;gap:8px;margin-top:14px;font-family:"Shippori Mincho",serif;font-size:15px;font-weight:700;color:#fff}
.org i{width:22px;height:22px;border-radius:50%;background:var(--gold);flex:none}
.note{margin-top:14px;font-size:11.5px;line-height:1.5;color:var(--gold-light);border-top:1px solid var(--gold);padding-top:6px}
.form{position:absolute;left:0;bottom:0;width:846px;height:190px;background:var(--cream);color:var(--ink);font-family:"Noto Sans JP",sans-serif;padding:14px 24px}
.form h2{font-size:14px;font-weight:700;color:var(--wine);margin-bottom:6px}
.form table{width:100%;border-collapse:collapse}
.form td{border:1px solid var(--line);height:62px;font-size:14px;padding:0 10px;vertical-align:middle}
.form td.head{width:90px;background:#f1e4c4;font-weight:700;text-align:center}
.form td.furi{font-size:10px;vertical-align:top;padding-top:2px;color:#8a7a66}
.form td.blank{width:190px}
</style>
</head>
<body>
<div class="flyer">
  <div class="stage"></div>
  <div class="portrait" role="img" aria-label="作曲家ヴェルナスキの肖像画"></div>
  <div class="piano" role="img" aria-label="グランドピアノの写真"></div>
  <div class="frame"></div>

  <p class="kicker">聴いて・知って・楽しめる</p>
  <p class="lead">今から約200年前（日本では江戸後期）に、わずか39歳でこの世を去った<br>ヴェルナスキの一生を、演奏と共に、彼が実際に書いた手紙内容を紹介します。</p>

  <h1 class="title"><span class="en">Stars and Prayer</span><span class="l1">星と祈りの</span><span class="l2">ロマンティック・ヴェルナスキ</span></h1>

  <ul class="timeline">
    <li><span class="age">8歳</span>大好きなパパ 手紙として愛情を一生懸命伝える</li>
    <li><span class="age">16歳</span>「僕に日曜日も働けというのは馬鹿げています」</li>
    <li><span class="age">17歳</span>「ぼくの健康は病気がち」</li>
    <li><span class="age">19歳</span>理想の女性を見出したんだ</li>
    <li><span class="age">20歳</span>「ぼくはいつも、君への想いに溢れ…」</li>
    <li><span class="age">21歳</span>「僕は眠れずに、ピアノの上に涙を」</li>
    <li><span class="age">26歳</span>「なんと恐ろしい思いをしたのだろう」</li>
  </ul>
  <p class="finale">―そして死の間際は・・・</p>

  <div class="info">
    <div class="row"><span class="label">日時</span><span class="date">2015年6月30日<small>(火)</small></span><span class="time">開場 13:00 ／ 開演 13:30</span></div>
    <div class="row"><span class="label">会場</span><span class="val"><strong>みなと芸術文化会館 そよかぜ小ホール</strong>（水辺県みなと市青葉町3丁目5-12）</span></div>
    <div class="row"><span class="label">出演</span><span class="val">一般社団法人 日本ふわりキーボード会 代表理事 <strong>森下 千秋</strong>（大阪翠嶺大学 卒）</span></div>
    <div class="row"><span class="label">曲目</span><span class="val">ノクターン第2番、バラード第1番、ポロネーズ第6番「英雄」ほか</span></div>
    <div class="row"><span class="label">参加料</span><span class="fee">3,240円</span><span class="val">（税込）</span></div>

    <div class="org"><i></i>一般社団法人 日本ふわりキーボード会</div>

    <p class="note">「ふわりキーボード」講師養成講座やセミナー参加で、ピアノの基礎とヴェルナスキの魅力を学べます。お問い合わせ 0120-000-000 ／ http://www.fuwarikbd.jp 又は「ふわりキーボード」で検索。<br>「気軽・喜び・集い」の音楽を！ 皆さまのご来場を心よりお待ちしております。</p>
  </div>

  <section class="form">
    <h2>参加申込書（6月7日）　締切必着</h2>
    <table>
      <tr><td class="head">お名前</td><td class="furi">フリガナ</td><td class="head">注文枚数</td><td class="blank"></td></tr>
      <tr><td class="head">電話番号</td><td></td><td class="head">合計金額</td><td class="blank"></td></tr>
    </table>
  </section>
</div>
</body>
</html>
```